Maple Syrup Bottle (front) Label design

I need label design for a 16fl OZ rectangular bottle of maple syrup with the usable dimensions of: Front: 4" x 2" and the back area for "ingredient specifications" of: 6" x 2". The maple syrup product comes from our own farm and is a quality product. The technical name/class of the syrup is: Grade A / AMBER
Updates

I can’t seem to find a way to upload a photo of the maple syrup bottle, but the front dimensions are clearly written on bottle description. Again: 4.5” by 2.25”

I have tried to upload the photo of the maple syrup bottle several times, and it seems (from my side) that it is successful. But I can never find it and the artists cannot find it either. Not sure what to do.

I have tried several times to add a photo of maple bottle, but it never shows up

This seems to be a futile exercise

I would like to post some images of the actual quill Hollow (not the one on Fendix, though!
But I can’t get back to the page that allows that to happen. Please advise!

Somebody PLEASE ask PW management to make it possible for me to upload more images! The "add photos" etc. just disappears from anywhere.

Target Market(s)

High-end food stores

Industry/Entity Type

Maple syrup retail industry

Other font styles liked:
• I don't know, and welcome suggestions

Colors

Designer to choose colors to be used in the design.

Requirements
Must have
• Name of Farm: Quill Hollow Maple
Nice to have
• The label can be "minimalist" and elegant. There is already a Maple leaf glass relief on the top of front of the bottle.
Should not have
• and NOT include farm buildings with steam coming out the chimney, etc.

```html
<!DOCTYPE html>
<html lang="en">
<head>
<meta charset="utf-8">
<title>Quill Hollow Maple – Front Label</title>
<link rel="stylesheet" href="https://fonts.googleapis.com/css2?family=Cinzel:wght@400&family=Lexend:wght@600&family=Italianno&display=swap">
<style>
  :root {
    --backdrop: #f2ede5;
    --label: #ffffff;
    --ink: #111111;
    --rule: #555555;
    --grade-red: #c8161d;
    --amber-light: #f7b23a;
    --amber-deep: #e2780f;
  }
  * { margin: 0; padding: 0; box-sizing: border-box; }
  html, body {
    width: 1200px;
    height: 1200px;
    overflow: hidden;
    background: var(--backdrop);
  }
  .canvas {
    position: relative;
    width: 1200px;
    height: 1200px;
  }
  .label {
    position: absolute;
    left: 320px;
    top: 40px;
    width: 560px;
    height: 1120px;
    background: var(--label);
    box-shadow: 0 2px 14px rgba(0,0,0,0.08);
  }
  .divider {
    position: absolute;
    left: 70px;
    width: 420px;
    height: 24px;
  }
  .divider--top { top: 36px; }
  .divider--bottom { top: 1060px; }
  .farm-name {
    position: absolute;
    top: 90px;
    left: 0;
    width: 100%;
    text-align: center;
    font-family: "Lexend", sans-serif;
    font-weight: 600;
    font-size: 40px;
    line-height: 52px;
    color: var(--ink);
  }
  .grade {
    position: absolute;
    top: 268px;
    left: 0;
    width: 100%;
    text-align: center;
    font-family: "Cinzel", serif;
    font-weight: 400;
    font-size: 60px;
    line-height: 80px;
    color: var(--grade-red);
    white-space: nowrap;
  }
  .tagline {
    position: absolute;
    top: 364px;
    left: 0;
    width: 100%;
    text-align: center;
    font-family: "Italianno", cursive;
    font-size: 62px;
    line-height: 80px;
    color: var(--ink);
  }
  .drop-illustration {
    position: absolute;
    left: 142px;
    top: 496px;
    width: 276px;
    height: 466px;
    background: linear-gradient(180deg, var(--amber-light) 0%, var(--amber-deep) 100%);
  }
</style>
</head>
<body>
<div class="canvas">
  <section class="label">
    <svg class="divider divider--top" viewBox="0 0 420 24" aria-hidden="true">
      <line x1="0" y1="12" x2="182" y2="12" stroke="var(--rule)" stroke-width="1.3"/>
      <line x1="238" y1="12" x2="420" y2="12" stroke="var(--rule)" stroke-width="1.3"/>
      <g fill="var(--ink)">
        <rect x="206" y="2" width="6" height="6" transform="rotate(45 209 5)"/>
        <rect x="206" y="16" width="6" height="6" transform="rotate(45 209 19)"/>
        <rect x="199" y="9" width="6" height="6" transform="rotate(45 202 12)"/>
        <rect x="213" y="9" width="6" height="6" transform="rotate(45 216 12)"/>
      </g>
    </svg>

    <h1 class="farm-name">Quill Hollow Maple</h1>
    <h2 class="grade">Grade A / Amber</h2>
    <p class="tagline">Finest Maple Syrup</p>

    <div class="drop-illustration" role="img" aria-label="Illustration of a glossy amber maple syrup droplet"></div>

    <svg class="divider divider--bottom" viewBox="0 0 420 24" aria-hidden="true">
      <line x1="0" y1="12" x2="182" y2="12" stroke="var(--rule)" stroke-width="1.3"/>
      <line x1="238" y1="12" x2="420" y2="12" stroke="var(--rule)" stroke-width="1.3"/>
      <g fill="var(--ink)">
        <rect x="206" y="2" width="6" height="6" transform="rotate(45 209 5)"/>
        <rect x="206" y="16" width="6" height="6" transform="rotate(45 209 19)"/>
        <rect x="199" y="9" width="6" height="6" transform="rotate(45 202 12)"/>
        <rect x="213" y="9" width="6" height="6" transform="rotate(45 216 12)"/>
      </g>
    </svg>
  </section>
</div>
</body>
</html>
```